STAFFONLYを変更
カメラをよりシンプルに
サイズの相談
ベースはこちらに決定いたします
ありがとうございます。
みなさまありがとうございます
最後まで悩みましたが
よりシンプルなもので
非関係者の抑制効果が一番ありそうなものを採用いたしました
関係者以外立ち入り禁止 POP POPデザインの仕事の依頼
LumivexCloudを中心にクラウドサービスを使った業務用アプリケーション開発をメインに行っております。
C#によるASP.NETによるWeb開発が中心で、WPFデスクトップアプリ、Formアプリ、Xamarinモバイルアプリを採用しております。
ハタラクモリでは上記プログラミングのパートナーを主に募集しています。
■募集に応募される方へのお願い
継続したお取引が可能な方を探しております。
フリーランス(一人法人含む)の方か、副業の方へご発注することが多いです。チームや法人、オフショアフロントの方と経験上成功したことがないです。
メッセージ中心のため、意図が伝わらず、容易に音信不通になります。実際に会うこともなくシステム上契約不履行時の違約金もないため、仕方がないことと割り切っていますが、大勢の方とのやり取りをしてメンバー選定しているので悲しくなります。逆にこちらからのレスが滞りご迷惑をおかけることもあります。
またプロトタイプで進めている関係で、要求がアバウトになることがほとんど。指示が二転三転することも。そういったことに神経質でない方がよいです。
トラブルで多いのが、資源を渡した瞬間に音信不通になる、成果物なしで支払いを余儀なくされる、生産的なやり取りではなく感情的なメッセージが来る、などです。こちらの作業内容や指示方法にも問題があることがありますので、初回の方は一定期間小規模予算でお互いが問題ないことを確認いただいてから継続契約します。
時々Skypeなどの打ち合わせを前提とされる方がおりますが、クラウドソーシングの特性を生かすとできるだけ時間を合わせて行うことが少ないほうが生産的で、必要最低限とさせて頂けますと幸いです。逆に作業時間帯はお好きな時間、何曜日でも構いません。フリーランスの方には十分な稼働時間を期待する半面、副業やフルで作業できないけど優れた技術者の開発リソースを安価に得られることがクラウドソーシングの最大のメリットだと考えています。
最後に、同じ自己紹介文で多くの仕事に同じメッセージで応募される方が多数おります。募集要項読んでいただけてない方は辞退しています。
いろいろ書いて申し訳ありませんが、私の考えに賛同してくださる方、ぜひ一緒に仕事させてください!
クライアント目線で柔軟な対応が可能な方と楽しく一緒に仕事をしたいです!

```html
<!DOCTYPE html>
<html lang="ja">
<head>
<meta charset="utf-8">
<title>関係者以外立入禁止 POP</title>
<link rel="stylesheet" href="https://fonts.googleapis.com/css2?family=Noto+Sans+JP:wght@700;900&display=swap">
<style>
  :root {
    --sign-black: #000000;
    --sign-white: #ffffff;
    --sign-red: #e60012;
    --lens-grey: #bdbdbd;
  }
  html, body {
    margin: 0;
    padding: 0;
    width: 1200px;
    height: 418px;
    overflow: hidden;
    background: var(--sign-black);
  }
  .sign {
    display: block;
    width: 1200px;
    height: 418px;
  }
  .sign__frame {
    fill: none;
    stroke: var(--sign-white);
    stroke-width: 6;
  }
  .sign__slash {
    stroke: var(--sign-red);
    stroke-width: 5;
  }
  .camera__body { fill: var(--sign-white); }
  .camera__seam { stroke: var(--sign-black); stroke-width: 3; }
  .camera__lens-ring { fill: var(--lens-grey); }
  .camera__lens-core { fill: var(--sign-black); }
  .camera__lens-glint { fill: var(--sign-white); }
  .sign__headline {
    font-family: "Noto Sans JP", sans-serif;
    font-weight: 900;
    font-size: 148px;
    fill: var(--sign-white);
  }
  .sign__notice {
    font-family: "Noto Sans JP", sans-serif;
    font-weight: 900;
    font-size: 46px;
    fill: var(--sign-white);
  }
  .sign__notice-accent { fill: var(--sign-red); }
</style>
</head>
<body>
<svg class="sign" viewBox="0 0 1200 418" xmlns="http://www.w3.org/2000/svg">
  <rect class="sign__frame" x="16" y="12" width="1168" height="394"/>
  <line class="sign__slash" x1="22" y1="402" x2="1181" y2="16"/>

  <g class="camera">
    <rect class="camera__body" x="136" y="15" width="176" height="30"/>
    <path class="camera__body" d="M146 45 H302 A78 88 0 0 1 146 45 Z"/>
    <line class="camera__seam" x1="146" y1="45" x2="302" y2="45"/>
    <circle class="camera__lens-ring" cx="216" cy="98" r="17"/>
    <circle class="camera__lens-core" cx="216" cy="98" r="10"/>
    <circle class="camera__lens-glint" cx="212" cy="94" r="3"/>
  </g>

  <text class="sign__headline" x="70" y="256" textLength="1040" lengthAdjust="spacingAndGlyphs">MENBERS ONLY</text>

  <text class="sign__notice" x="646" y="338" textLength="470" lengthAdjust="spacing">関係者以外立入<tspan class="sign__notice-accent">禁</tspan>止</text>
</svg>
</body>
</html>
```